Commercial janitorial cleaning

Janitorial cleaning particularly for commercial buildings. Website needs to specify free estimates. Location of service is Hudson, Valatie, East Greenbush, Troy, Albany ny area. Services page with Janitorial services- General Office Cleaning, Construction Cleaning, Carpet Extraction, Consultation/Business, Lighting Maintenance, Seasonal Deep Cleaning, Window cleaning, Event Cleaning, Floor and Carpet Cleaning, Floor Striping and Waxing. Contact us page with email phone number on page and a request page that emails me if they have any questions. About us page-the picture of my family on it with a section I can type a story myself.

Target Market(s)

Commercial businesses

Industry/Entity Type

Janitorial Service

Number of Pages Required

4 page

Font styles to use
Serif
Sans Serif
Script

Colors
ec1f27
1b1b1b
ffffff
9d9d9d

Requirements
Must have
• Phone number 555-304-7162. Must have free estimates on home page. Going for industrial / modern look to website
Nice to have
• Logo is a red and black building so if those colors could be coordinated to website that would be awesome.

```html
<!DOCTYPE html>
<html lang="en">
<head>
<meta charset="utf-8">
<title>Brightline Cleaning Services</title>
<link rel="stylesheet" href="https://fonts.googleapis.com/css2?family=Open+Sans:ital,wght@0,400;0,600;0,700;1,400;1,700&family=Roboto+Condensed:wght@400;700&display=swap">
<style>
:root{
  --red:#ec1f27;
  --ink:#1b1b1b;
  --white:#ffffff;
  --grey:#9d9d9d;
  --text:#555555;
  --pale:#f1f0f1;
  --head:'Roboto Condensed',Arial,sans-serif;
  --body:'Open Sans',Arial,sans-serif;
}
*{box-sizing:border-box;margin:0;padding:0}
html,body{width:1200px;height:2761px;overflow:hidden;background:var(--white)}
body{position:relative;font-family:var(--body);color:var(--ink)}
.abs{position:absolute}

/* header */
.top-rule{left:0;top:0;width:1200px;height:4px;background:var(--red)}
.brand{left:98px;top:22px;display:flex;align-items:center;gap:10px}
.brand-mark{width:52px;height:60px;background:var(--red)}
.brand-name{font-weight:600;color:var(--red);font-size:21px;line-height:24px}
.brand-name small{display:block;font-size:13px;line-height:18px}
.contact-line{top:22px;left:562px;display:flex;align-items:center;font-size:14px;color:#444}
.contact-line .ic{width:26px;height:26px;border-radius:50%;display:inline-flex;align-items:center;justify-content:center;margin-right:10px}
.contact-line .ic.red{background:var(--red)}
.contact-line .ic.dark{background:var(--ink)}
.contact-item{display:flex;align-items:center;margin-right:22px}
.login{left:1010px;top:23px;width:90px;height:31px;border:1.5px solid var(--red);border-radius:4px;color:var(--red);font-size:11px;font-weight:600;display:flex;align-items:center;justify-content:center;gap:5px}
.nav{left:360px;top:70px;display:flex}
.nav a{font-size:16px;color:var(--ink);text-decoration:none;padding:0 21px}
.nav a.current{color:var(--red)}

/* hero */
.hero{left:0;top:105px;width:1200px;height:478px;background:linear-gradient(90deg,#c9cdd1 0%,#dfe2e5 30%,#e2e4e6 70%,#c6cacf 100%)}
.hero-sign{left:400px;top:105px;width:290px;height:478px;background:linear-gradient(180deg,#f4b81c,#e8a40e)}
.hero-title{left:98px;top:234px;font-family:var(--head);font-weight:700;font-size:40px;line-height:48px;color:var(--ink)}
.btn-solid{background:var(--red);color:var(--white);font-weight:700;display:flex;align-items:center;justify-content:center;text-transform:uppercase}
.hero-btn{left:98px;top:348px;width:150px;height:52px;font-size:13px}
.dots{left:98px;top:430px;display:flex;gap:8px}
.dots span{width:11px;height:11px;border-radius:50%;background:var(--white)}
.dots span.on{background:var(--red)}

/* services */
.services{left:0;top:583px;width:1200px;height:597px;background:var(--pale)}
.section-title{font-family:var(--head);font-weight:400;font-size:28px;color:var(--ink);text-transform:uppercase}
.services .section-title{position:absolute;left:0;width:1200px;top:64px;text-align:center}
.services-intro{position:absolute;left:212px;width:776px;top:112px;text-align:center;font-size:11.5px;line-height:23px;color:var(--text)}
.card{position:absolute;top:206px;width:230px;height:223px}
.card-photo{width:230px;height:182px}
.card-label{position:absolute;left:0;bottom:0;width:230px;height:60px}
.card-label svg{position:absolute;left:0;top:0}
.card-label span{position:relative;display:flex;height:60px;padding-top:8px;align-items:center;justify-content:center;text-align:center;color:var(--white);font-weight:700;font-size:13.5px;line-height:21px;text-transform:uppercase}
.btn-line{border:1.5px solid var(--red);color:var(--red);background:var(--white);font-size:12.5px;display:flex;align-items:center;justify-content:center;text-transform:uppercase}
.all-services{position:absolute;left:524px;top:482px;width:152px;height:45px}

/* welcome */
.welcome-photo{left:80px;top:1222px;width:400px;height:336px;background:linear-gradient(180deg,#f7f1ef 0%,#f1e3df 100%)}
.welcome-title{left:515px;top:1246px;font-size:25px}
.welcome-copy{left:515px;top:1310px;width:590px;font-size:11.8px;line-height:22.5px;color:var(--text)}
.welcome-copy p+p{margin-top:4px}
.welcome-more{left:515px;top:1498px;width:102px;height:40px}
.welcome-contact{left:626px;top:1498px;width:108px;height:40px;font-size:12.5px;font-weight:600}

/* stats */
.stats{left:0;top:1605px;width:1200px;height:256px;background:var(--red)}
.stat{position:absolute;top:50px;width:220px;margin-left:-110px;text-align:center;color:var(--white)}
.stat-icon{width:74px;height:74px;border:2px solid var(--white);border-radius:50%;margin:0 auto;display:flex;align-items:center;justify-content:center}
.stat-num{font-weight:700;font-size:34px;line-height:40px;margin-top:12px}
.stat-label{font-size:15px;line-height:22px}

/* blog + testimonial */
.col-title{font-size:22px}
.col-rule{width:52px;height:3px;background:var(--red)}
.post{position:absolute;top:2017px;width:243px}
.post-photo{width:243px;height:179px;border:5px solid #e4e4e4}
.post-title{margin-top:24px;font-size:14px;color:var(--ink);text-transform:uppercase}
.post-excerpt{margin-top:8px;font-size:11px;line-height:19px;color:var(--text)}
.post .btn-line{margin-top:14px;width:96px;height:30px;font-size:11px}
.quote-box{left:651px;top:2019px;width:449px;height:302px;background:#f4f4f4;overflow:hidden}
.quote-text{position:absolute;left:20px;top:38px;width:330px;font-style:italic;font-size:12.3px;line-height:24px;color:var(--text)}
.quote-name{position:absolute;left:20px;top:150px;font-style:italic;font-weight:700;font-size:15px;color:var(--red)}
.quote-role{position:absolute;left:20px;top:176px;font-size:13px;color:var(--text)}
.quote-dots{position:absolute;left:20px;top:206px;display:flex;gap:6px}
.quote-dots span{width:8px;height:8px;border-radius:50%;background:#cfcfcf}
.quote-dots span.on{background:var(--red)}
.quote-photo{position:absolute;left:300px;top:114px;width:135px;height:188px;background:#4a3a3c}

/* footer */
.footer{left:0;top:2401px;width:1200px;height:360px;background:#161616}
.f-col{position:absolute;top:58px;color:var(--white)}
.f-head{font-family:var(--head);font-weight:700;font-size:15px;text-transform:uppercase;margin-bottom:20px}
.f-row{display:flex;gap:14px;font-size:12px;line-height:19px;margin-bottom:16px}
.f-list{list-style:none;font-size:12px;line-height:24px}
.f-list li::before{content:"›";font-weight:700;margin-right:10px}
.social{display:flex;gap:8px;margin-top:6px}
.social span{width:26px;height:26px;border:1.5px solid var(--white);border-radius:50%}
.f-note{font-size:11px;line-height:19px;width:270px}
.f-input{margin-top:18px;width:270px;height:40px;background:var(--white);color:#444;font-size:11px;padding:0 12px;display:flex;align-items:center}
.f-sub{margin-top:14px;width:100px;height:40px;font-size:12px}
.copyright{left:0;top:2715px;width:1200px;text-align:center;color:var(--white);font-size:12px}
</style>
</head>
<body>

<header>
  <div class="abs top-rule"></div>
  <div class="abs brand">
    <div class="brand-mark"></div>
    <div class="brand-name">Brightline<small>Cleaning Services</small></div>
  </div>
  <div class="abs contact-line">
    <div class="contact-item"><span class="ic red"><svg width="13" height="13" viewBox="0 0 24 24"><path fill="#fff" d="M6.6 10.8a15 15 0 0 0 6.6 6.6l2.2-2.2c.3-.3.7-.4 1-.2 1.1.4 2.3.6 3.6.6.6 0 1 .4 1 1V20c0 .6-.4 1-1 1A17 17 0 0 1 3 4c0-.6.4-1 1-1h3.5c.6 0 1 .4 1 1 0 1.3.2 2.5.6 3.6.1.3 0 .7-.2 1z"/></svg></span>555-304-7162</div>
    <div class="contact-item"><span class="ic dark"><svg width="13" height="13" viewBox="0 0 24 24"><path fill="#fff" d="M3 5h18v14H3z"/><path d="M3 5l9 8 9-8" fill="none" stroke="#1b1b1b" stroke-width="2"/></svg></span>hello@brightlinecleaning.com</div>
  </div>
  <div class="abs login"><svg width="10" height="11" viewBox="0 0 10 11"><rect x="1" y="5" width="8" height="6" fill="#ec1f27"/><path d="M3 5V3a2 2 0 0 1 4 0v2" fill="none" stroke="#ec1f27" stroke-width="1.5"/></svg>LOG-IN</div>
  <nav class="abs nav">
    <a class="current">Home</a><a>About us</a><a>Services</a><a>Gallery</a><a>Testimonials</a><a>Blog</a><a>Contact us</a>
  </nav>
</header>

<section>
  <div class="abs hero" role="img" aria-label="Bright office corridor with a yellow wet floor caution sign"></div>
  <div class="abs hero-sign" role="img" aria-label="Yellow caution wet floor sign"></div>
  <h1 class="abs hero-title">MAKE YOUR WORLD AS<br>CLEAN AS MINE</h1>
  <div class="abs btn-solid hero-btn">Free Estimate</div>
  <div class="abs dots"><span class="on"></span><span></span><span></span><span></span></div>
</section>

<section class="abs services">
  <h2 class="section-title">What We Do</h2>
  <p class="services-intro">All the Lorem Ipsum generators on the Internet tend to repeat predefined chunks as necessary, making this the first true generator on the Internet. It uses a dictionary of over 200 Latin words, combined with a handful of model sentence</p>

  <div class="card" style="left:98px">
    <div class="card-photo" role="img" aria-label="Caution sign on a polished office floor" style="background:linear-gradient(180deg,#d3d6d9 0%,#d9b552 100%)"></div>
    <div class="card-label"><svg width="230" height="60"><polygon points="0,8 115,0 230,8 230,60 0,60" fill="#ec1f27"/></svg><span>General<br>Office Cleaning</span></div>
  </div>
  <div class="card" style="left:357px">
    <div class="card-photo" role="img" aria-label="Janitorial cart with yellow bins" style="background:linear-gradient(180deg,#e3e6e9 0%,#c3c7cc 100%)"></div>
    <div class="card-label"><svg width="230" height="60"><polygon points="0,8 115,0 230,8 230,60 0,60" fill="#ec1f27"/></svg><span>Construction<br>Cleaning</span></div>
  </div>
  <div class="card" style="left:616px">
    <div class="card-photo" role="img" aria-label="Cleaner vacuuming a floor" style="background:linear-gradient(180deg,#e9e9eb 0%,#b7bcc6 100%)"></div>
    <div class="card-label"><svg width="230" height="60"><polygon points="0,8 115,0 230,8 230,60 0,60" fill="#ec1f27"/></svg><span>Seasonal<br>Deep Cleaning</span></div>
  </div>
  <div class="card" style="left:872px">
    <div class="card-photo" role="img" aria-label="Worker waxing a wooden floor" style="background:linear-gradient(180deg,#b07a4c 0%,#8c5a34 100%)"></div>
    <div class="card-label"><svg width="230" height="60"><polygon points="0,8 115,0 230,8 230,60 0,60" fill="#ec1f27"/></svg><span>Floor Striping<br>and Waxing</span></div>
  </div>

  <div class="btn-line all-services">View All Services</div>
</section>

<section>
  <div class="abs welcome-photo" role="img" aria-label="Cleaner kneeling beside a red bucket wiping the floor"></div>
  <h2 class="abs section-title welcome-title">Welcome To Our Company</h2>
  <div class="abs welcome-copy">
    <p>There are many variations of passages of Lorem Ipsum available, but the majority have suffered alteration in some form, by injected humour, or randomised you need to be sure words which don't look even slightly believable. If you are going to use a passage of Lorem Ipsum, you need to be sure there isn't anything embarrassing hidden in the middle of text.</p>
    <p>There are many variations of passages of Lorem Ipsum available, but the majority have suffered alteration in some form, by injected humour, or randomised you need to be sure words which don't look even slightly believable. If you are going to use a passage of Lorem Ipsum.</p>
  </div>
  <div class="abs btn-line welcome-more">Read More</div>
  <div class="abs btn-solid welcome-contact">Contact Us</div>
</section>

<section class="abs stats">
  <div class="stat" style="left:252px">
    <div class="stat-icon"><svg width="38" height="32" viewBox="0 0 38 32" fill="#fff"><circle cx="19" cy="7" r="5"/><circle cx="8" cy="11" r="4"/><circle cx="30" cy="11" r="4"/><path d="M11 30c0-7 4-11 8-11s8 4 8 11z"/><path d="M1 30c0-6 3-9 7-9 2 0 3 1 4 2-2 2-3 4-3 7z"/><path d="M37 30c0-6-3-9-7-9-2 0-3 1-4 2 2 2 3 4 3 7z"/></svg></div>
    <div class="stat-num">3490</div><div class="stat-label">Satisfied Customers</div>
  </div>
  <div class="stat" style="left:486px">
    <div class="stat-icon"><svg width="34" height="32" viewBox="0 0 34 32" fill="#fff"><rect x="4" y="4" width="26" height="27"/><g fill="#ec1f27"><rect x="8" y="8" width="4" height="4"/><rect x="15" y="8" width="4" height="4"/><rect x="22" y="8" width="4" height="4"/><rect x="8" y="15" width="4" height="4"/><rect x="15" y="15" width="4" height="4"/><rect x="22" y="15" width="4" height="4"/><rect x="14" y="23" width="6" height="8"/></g></svg></div>
    <div class="stat-num">4530</div><div class="stat-label">Building Cleaned</div>
  </div>
  <div class="stat" style="left:721px">
    <div class="stat-icon"><svg width="36" height="32" viewBox="0 0 36 32" fill="none" stroke="#fff" stroke-width="3" stroke-linecap="round"><circle cx="22" cy="6" r="3.5" fill="#fff" stroke="none"/><path d="M20 11l-6 8 8 3-2 8"/><path d="M14 19L6 26"/><path d="M20 11l8 5"/><path d="M4 30h28"/></svg></div>
    <div class="stat-num">4390</div><div class="stat-label">Clever Employees</div>
  </div>
  <div class="stat" style="left:955px">
    <div class="stat-icon"><svg width="34" height="32" viewBox="0 0 34 32" fill="#fff"><polygon points="17,2 32,10 2,10"/><rect x="6" y="12" width="3" height="14"/><rect x="12" y="12" width="3" height="14"/><rect x="19" y="12" width="3" height="14"/><rect x="25" y="12" width="3" height="14"/><rect x="2" y="27" width="30" height="4"/></svg></div>
    <div class="stat-num">2490</div><div class="stat-label">Office World Wide</div>
  </div>
</section>

<section>
  <h2 class="abs section-title col-title" style="left:99px;top:1926px">Our Blog Posts</h2>
  <div class="abs col-rule" style="left:99px;top:1973px"></div>
  <h2 class="abs section-title col-title" style="left:651px;top:1926px">What Our Client's Say</h2>
  <div class="abs col-rule" style="left:651px;top:1973px"></div>

  <article class="post" style="left:99px">
    <div class="post-photo" role="img" aria-label="Clean bright room with wooden floor" style="background:linear-gradient(180deg,#e6e3df 0%,#c9a27c 100%)"></div>
    <div class="post-title">Lorem Ipsum Dolor</div>
    <p class="post-excerpt">Sed ut perspiciatis unde omnis iste natuaccu-santium doloremque bum,</p>
    <div class="btn-line">Read More ⊕</div>
  </article>
  <article class="post" style="left:374px">
    <div class="post-photo" role="img" aria-label="Yellow cleaning sign in an office" style="background:linear-gradient(180deg,#5f646b 0%,#a7a9a6 100%)"></div>
    <div class="post-title">Lorem Ipsum Dolor</div>
    <p class="post-excerpt">Sed ut perspiciatis unde omnis iste natuaccu-santium doloremque bum,</p>
    <div class="btn-line">Read More ⊕</div>
  </article>

  <div class="abs quote-box">
    <svg class="abs" style="left:0;top:0" width="449" height="302"><polygon points="449,0 449,302 150,302" fill="#ec1f27"/></svg>
    <p class="quote-text">“ Sed ut perspiciatis unde omnis iste natus error sit voluptatem accusantium doloremque laudantium, oluptatem accusantium doloremquetotam rem aperiam, eaque ipsa quae ab illo inventore verita ”</p>
    <div class="quote-name">-Maren Holt</div>
    <div class="quote-role">Founder of company</div>
    <div class="quote-dots"><span class="on"></span><span></span><span></span></div>
    <div class="quote-photo" role="img" aria-label="Family portrait of the company founder"></div>
  </div>
</section>

<footer class="abs footer">
  <div class="f-col" style="left:99px;width:300px">
    <div class="f-head">Contact Us</div>
    <div class="f-row"><svg width="14" height="18" viewBox="0 0 14 18"><path d="M7 1a6 6 0 0 1 6 6c0 4-6 10-6 10S1 11 1 7a6 6 0 0 1 6-6z" fill="none" stroke="#fff" stroke-width="1.5"/><circle cx="7" cy="7" r="2" fill="#fff"/></svg><span>42 Harbor Lane, Suite 5,<br>Hudson NY 12534</span></div>
    <div class="f-row"><svg width="14" height="14" viewBox="0 0 24 24"><path fill="none" stroke="#fff" stroke-width="2" d="M6.6 10.8a15 15 0 0 0 6.6 6.6l2.2-2.2c.3-.3.7-.4 1-.2 1.1.4 2.3.6 3.6.6.6 0 1 .4 1 1V20c0 .6-.4 1-1 1A17 17 0 0 1 3 4c0-.6.4-1 1-1h3.5c.6 0 1 .4 1 1 0 1.3.2 2.5.6 3.6.1.3 0 .7-.2 1z"/></svg><span>Phone : 555-304-7162</span></div>
    <div class="f-row"><svg width="15" height="12" viewBox="0 0 15 12"><rect x="1" y="1" width="13" height="10" fill="none" stroke="#fff" stroke-width="1.3"/><path d="M1 1l6.5 5L14 1" fill="none" stroke="#fff" stroke-width="1.3"/></svg><span>hello@brightlinecleaning.com</span></div>
    <div class="social"><span></span><span></span><span></span><span></span></div>
  </div>
  <div class="f-col" style="left:445px">
    <div class="f-head">Quick Links</div>
    <ul class="f-list"><li>Home</li><li>About Us</li><li>Our Services</li><li>Testimonials</li><li>Blog</li><li>Contact Us</li></ul>
  </div>
  <div class="f-col" style="left:633px">
    <div class="f-head">Other Links</div>
    <ul class="f-list"><li>Advice&amp;Tips</li><li>News&amp;video</li><li>Our Services</li><li>Privacy policy</li><li>Terms&amp;conditions</li><li>Sitemap</li></ul>
  </div>
  <div class="f-col" style="left:830px">
    <div class="f-head">Sign Up To Newsletter</div>
    <p class="f-note">Excepteur sint occaecat cupidatat non proident, sunt in culpa qui Nemo enim</p>
    <div class="f-input">Enter Name</div>
    <div class="btn-solid f-sub">Subscribe</div>
  </div>
</footer>
<div class="abs copyright">Copyright © Brightline Cleaning Services 2017. All rights reserved.</div>

</body>
</html>
```